Adventurous female pilot

I am looking for a personal business card, for a very well qualified female pilot, with a lot of aviation experience.

Currently an airline pilot, have worked as a bush pilot in Africa, looking to get into corporate aviation, or private jet owners.
Want a classy looking card for networking...

Could be interested in a retro\vintage look also?!

An idea,, is an african sunset background, with my wings\logo on it
Updates

I just want to say thank you to all of your for your amazing designs!

I have been very busy flying this past week , so not had a chance to be on the computer much.
But I provide some feedback, and conclusions very soon!
Thank you again.

Marla

Reason: Still waiting on a couple of revisions to be 100% about my choice!

Target Market(s)

corporate aviation, private jet owners, casino's,
General audience.
networking

Industry/Entity Type

Airline

Requirements
Nice to have
• Classy, edgy, sexy, but also feminine

```html
<!DOCTYPE html>
<html lang="en">
<head>
<meta charset="utf-8">
<title>Marla Vance — Business Card</title>
<link href="https://fonts.googleapis.com/css2?family=Parisienne&display=swap" rel="stylesheet">
<style>
  :root {
    --page-bg: #ece6dc;
    --sky-deep: #5a1606;
    --sky-mid: #b3470c;
    --sky-glow: #f2a21a;
    --sun: #f7b63a;
    --ground: #1e0804;
    --figure-tone: #c77a3e;
    --figure-light: #e7b58a;
    --ink: #ffffff;
    --card-shadow: rgba(40, 25, 10, 0.35);
  }
  * { box-sizing: border-box; margin: 0; padding: 0; }
  html, body {
    width: 1200px;
    height: 1000px;
    overflow: hidden;
    background: var(--page-bg);
  }
  .canvas {
    position: relative;
    width: 1200px;
    height: 1000px;
  }
  .business-card {
    position: absolute;
    left: 120px;
    top: 225px;
    width: 960px;
    height: 550px;
    border-radius: 10px;
    overflow: hidden;
    box-shadow: 0 18px 40px var(--card-shadow);
    font-family: "Parisienne", cursive;
    color: var(--ink);
  }
  .sunset-scene {
    position: absolute;
    inset: 0;
    background:
      radial-gradient(circle at 50% 28%, var(--sun) 0 17%, transparent 32%),
      linear-gradient(180deg, var(--sky-deep) 0%, var(--sky-mid) 30%, var(--sky-glow) 58%, var(--sky-mid) 76%, var(--ground) 92%);
  }
  .ground-band {
    position: absolute;
    left: 0; right: 0; bottom: 0;
    height: 16%;
    background: linear-gradient(180deg, rgba(30, 8, 4, 0.6), var(--ground));
  }
  .pilot-portrait {
    position: absolute;
    left: 6%;
    top: 6%;
    width: 34%;
    height: 80%;
    border-radius: 46% 46% 8px 8px / 30% 30% 8px 8px;
    background: linear-gradient(180deg, var(--figure-light) 0%, var(--figure-tone) 55%, rgba(199, 122, 62, 0.4) 100%);
    opacity: 0.85;
  }
  .brand-mark {
    position: absolute;
    left: 57%;
    top: 19%;
    width: 40%;
    text-align: center;
    font-size: 54px;
    line-height: 1;
  }
  .holder-name {
    position: absolute;
    left: 53%;
    top: 60%;
    font-size: 42px;
    line-height: 1;
  }
  .holder-email {
    position: absolute;
    left: 53%;
    top: 69%;
    font-size: 31px;
    line-height: 1;
  }
  .phone-us {
    position: absolute;
    left: 4%;
    top: 77%;
    font-size: 31px;
    line-height: 1;
  }
  .phone-taipei {
    position: absolute;
    left: 51%;
    top: 84%;
    font-size: 31px;
    line-height: 1;
  }
</style>
</head>
<body>
  <main class="canvas">
    <article class="business-card">
      <div class="sunset-scene" role="img" aria-label="African savanna at sunset with acacia trees, an elephant and giraffes in silhouette"></div>
      <div class="ground-band"></div>
      <div class="pilot-portrait" role="img" aria-label="Illustrated female pilot with long hair, sunglasses and an open-collared shirt"></div>
      <div class="brand-mark">Vance Aviation</div>
      <h1 class="holder-name" style="font-weight:400">Marla Vance</h1>
      <p class="holder-email">Email: marlacvance@skymail.net</p>
      <p class="phone-us">Cell US: +1 702-555-0143</p>
      <p class="phone-taipei">Cell Taipei: +886 970-555-214</p>
    </article>
  </main>
</body>
</html>
```